Brookfarrow Osteopathy and dry needling business card

Business card for Brookfarrow Osteopathy and Dry Needling.

Industry/Entity Type

Health

Contact Information for Business Card

I do not have a phone number yet. I also do not have an email address yet. The physical address is: 48 Lower Crane Street Brookfarrow The website is: www.brookfarrowosteosteopathy.example My details are: Dr Martin Pellowe, Osteopath (B.Clin.Sci (Ost) M.Ost BSC ECON (Hons)

Colors
0094D4
00A9DD
6FCCEA
C7EBF8
E9F6FB

Requirements
Must have
• logo on the back
Nice to have
• Maybe a space for me to write an appointment time and date on the card.

```html
<!DOCTYPE html>
<html lang="en">
<head>
<meta charset="utf-8">
<title>Brookfarrow Osteopathy and Dry Needling – Business Card</title>
<link href="https://fonts.googleapis.com/css2?family=Arimo:wght@400;700&family=Montserrat:wght@500&display=swap" rel="stylesheet">
<style>
  :root {
    --brand-blue: #0094D4;
    --brand-sky: #00A9DD;
    --brand-light: #6FCCEA;
    --brand-pale: #C7EBF8;
    --brand-mist: #E9F6FB;
    --accent-orange: #F7931E;
    --ink: #3a3a3a;
    --muted: #555555;
    --page: #e4e4e4;
    --card: #ffffff;
  }
  * { margin: 0; padding: 0; box-sizing: border-box; }
  html, body { width: 1200px; height: 1200px; overflow: hidden; }
  body {
    background: var(--page);
    font-family: "Arimo", Arial, sans-serif;
    position: relative;
  }
  .card {
    position: absolute;
    background: var(--card);
    overflow: hidden;
    box-shadow: 0 14px 24px rgba(0,0,0,0.18);
  }

  /* Front */
  .card-front { left: 270px; top: 170px; width: 671px; height: 383px; }
  .brand-mark {
    position: absolute; left: 67px; top: 82px; width: 200px; height: 200px;
    display: flex; flex-direction: column; align-items: center; justify-content: center;
    text-align: center; gap: 12px;
  }
  .brand-mark .dot {
    width: 58px; height: 58px; border-radius: 50%;
    border: 3px solid var(--brand-blue);
  }
  .brand-mark .brand-name {
    color: var(--brand-blue); font-weight: 700; font-size: 17px; line-height: 1.25;
  }
  .divider {
    position: absolute; left: 291px; top: 85px; width: 2px; height: 195px;
    background: linear-gradient(to bottom, rgba(120,120,120,0), #8a8a8a 20%, #8a8a8a 80%, rgba(120,120,120,0));
  }
  .details { position: absolute; left: 310px; top: 90px; }
  .person-name { color: var(--brand-sky); font-weight: 700; font-size: 27px; line-height: 1; }
  .role { color: var(--accent-orange); font-size: 15.5px; line-height: 19px; margin-top: 6px; }
  .address { color: var(--ink); font-size: 16px; margin-top: 14px; }
  .contacts { list-style: none; margin-top: 17px; }
  .contacts li {
    display: flex; align-items: center; gap: 9px;
    color: var(--ink); font-size: 16px; line-height: 20px;
  }
  .contacts svg { width: 14px; height: 14px; flex: none; }
  .front-rule { position: absolute; left: 0; right: 0; top: 362px; height: 3px; background: var(--accent-orange); }
  .front-band { position: absolute; left: 0; right: 0; top: 366px; bottom: 0; background: var(--brand-sky); }

  /* Back */
  .card-back { left: 262px; top: 653px; width: 687px; height: 393px; }
  .watermark {
    position: absolute; left: 162px; top: 20px; width: 355px; height: 355px;
    border-radius: 50%; border: 3px solid var(--brand-mist);
  }
  .back-title {
    position: absolute; left: 46px; top: 49px;
    color: var(--brand-sky); font-family: "Montserrat", Arial, sans-serif; font-weight: 500; font-size: 26px;
  }
  .appointment-row {
    position: absolute; left: 46px; width: 595px;
    display: flex; align-items: baseline; color: var(--brand-sky); font-size: 17px;
  }
  .appointment-row .fill {
    border-bottom: 2px dotted #9aa6ad; height: 0; margin: 0 4px; transform: translateY(-3px);
  }
  .fill-date { flex: 0 0 318px; }
  .fill-time { flex: 1; }
  .row-1 { top: 124px; } .row-2 { top: 186px; } .row-3 { top: 249px; }
  .web-band {
    position: absolute; left: 0; right: 0; top: 313px; height: 24px;
    background: linear-gradient(to right, #1a5fb4, var(--brand-sky) 35%, var(--brand-sky) 65%, #1a5fb4);
    color: #fff; text-align: center; font-size: 16px; letter-spacing: 1.6px; line-height: 24px;
  }
  .cancel-note {
    position: absolute; left: 0; right: 0; top: 352px;
    text-align: center; color: var(--muted); font-size: 14px;
  }
</style>
</head>
<body>
  <section class="card card-front">
    <div class="brand-mark">
      <span class="dot"></span>
      <span class="brand-name">Brookfarrow Osteopathy<br>and Dry Needling</span>
    </div>
    <div class="divider"></div>
    <div class="details">
      <h1 class="person-name">Dr Martin Pellowe</h1>
      <p class="role">Osteopath<br>(B.Clin.Sci (Ost) M.Ost BSC ECON (Hons)</p>
      <p class="address">48 Lower Crane Street Brookfarrow</p>
      <ul class="contacts">
        <li>
          <svg viewBox="0 0 24 24"><path fill="#0094D4" d="M6.6 10.8a15.1 15.1 0 0 0 6.6 6.6l2.2-2.2c.3-.3.7-.4 1-.2 1.1.4 2.3.6 3.6.6.6 0 1 .4 1 1V20c0 .6-.4 1-1 1C10.6 21 3 13.4 3 4c0-.6.4-1 1-1h3.5c.6 0 1 .4 1 1 0 1.3.2 2.5.6 3.6.1.3 0 .7-.2 1z"/></svg>
          555-014-2287
        </li>
        <li>
          <svg viewBox="0 0 24 24"><rect x="2" y="5" width="20" height="14" fill="#0094D4"/><path d="M2 5l10 8 10-8" fill="none" stroke="#fff" stroke-width="2"/></svg>
          info@brookfarrowosteosteopathy.example
        </li>
        <li>
          <svg viewBox="0 0 24 24"><circle cx="12" cy="12" r="10" fill="#0094D4"/><path d="M7 8c2 1 3 3 2 5s1 3 2 5M15 5c-1 2 1 3 3 3m-4 5c2 0 3 2 3 4" fill="none" stroke="#fff" stroke-width="1.6"/></svg>
          brookfarrowosteosteopathy.example
        </li>
      </ul>
    </div>
    <div class="front-rule"></div>
    <div class="front-band"></div>
  </section>

  <section class="card card-back">
    <div class="watermark"></div>
    <h2 class="back-title">Next Appointment</h2>
    <div class="appointment-row row-1"><span>Date :</span><span class="fill fill-date"></span><span>Time :</span><span class="fill fill-time"></span><span>AM/PM</span></div>
    <div class="appointment-row row-2"><span>Date :</span><span class="fill fill-date"></span><span>Time :</span><span class="fill fill-time"></span><span>AM/PM</span></div>
    <div class="appointment-row row-3"><span>Date :</span><span class="fill fill-date"></span><span>Time :</span><span class="fill fill-time"></span><span>AM/PM</span></div>
    <div class="web-band">WWW.BROOKFARROWOSTEOSTEOPATHY.EXAMPLE</div>
    <p class="cancel-note">Please give 24 hours notice cancelling your appointment or a fee may be charged</p>
  </section>
</body>
</html>
```